IT Network Consultancy - Business Card

t4 linkways is a IT network consultancy based in London. We're looking for a smart, modern and professional business card design. Our website is here: www.t4linkways.co.uk

Key things that should be included on the card (with examples):

Company Logo
Name
Position / Job Title: Network Consultant
Mobile Phone Number: +44 (0) 7700 900418
Land Line: +44 (0) 1632 960274
Email Address: name@t4linkways.co.uk
Web Site URL: www.t4linkways.co.uk

Target Market(s)

Large enterprise / global companies / corporates

Industry/Entity Type

Business

Requirements
Must have
• Incorporate our logo - which is attached to the project. They are in AI format (can be opened in Inkscape).

The design should be double sided and fit on a UK standard 85mm × 55mm card and be in a format that retains the quality when printed.
Nice to have
• The project does not have to conform to the colour of our website but this should give you inspiration of the style we like.
Should not have
• Bright colours. Pictures are not necessary.

```html
<!DOCTYPE html>
<html lang="en">
<head>
<meta charset="utf-8">
<title>t4 linkways – Business Card</title>
<link rel="stylesheet" href="https://fonts.googleapis.com/css2?family=Open+Sans:wght@400;600;700&display=swap">
<style>
  :root {
    --page-bg: #ffffff;
    --card-front: #959ea5;
    --ink-dark: #4a535b;
    --ink-grey: #8f989f;
    --ink-light: #9ba3aa;
    --rule: #9aa2a8;
    --border: #a4aab0;
    --white: #ffffff;
  }
  * { margin: 0; padding: 0; box-sizing: border-box; }
  html, body {
    width: 1200px;
    height: 900px;
    overflow: hidden;
    background: var(--page-bg);
    font-family: "Open Sans", Arial, sans-serif;
  }
  .canvas {
    position: relative;
    width: 1200px;
    height: 900px;
  }
  .card {
    position: absolute;
    left: 282px;
    width: 572px;
    height: 390px;
    border-radius: 16px;
  }
  .card--front {
    top: 48px;
    background: var(--card-front);
  }
  .card--back {
    top: 464px;
    background: var(--white);
    border: 2px solid var(--border);
  }
  .front-brand {
    position: absolute;
    left: 0;
    right: 0;
    top: 146px;
    text-align: center;
    font-size: 62px;
    font-weight: 700;
    color: var(--ink-dark);
    letter-spacing: -1px;
  }
  .front-url {
    position: absolute;
    left: 0;
    right: 0;
    bottom: 4px;
    text-align: center;
    font-size: 22px;
    color: var(--ink-dark);
  }
  .back-brand {
    position: absolute;
    left: 40px;
    top: 140px;
    width: 190px;
    text-align: center;
    font-size: 34px;
    font-weight: 700;
    color: var(--ink-light);
    letter-spacing: -0.5px;
  }
  .back-rule {
    position: absolute;
    left: 244px;
    top: 102px;
    width: 3px;
    height: 176px;
    background: var(--rule);
  }
  .identity {
    position: absolute;
    left: 270px;
    top: 128px;
  }
  .identity__name {
    font-size: 36px;
    font-weight: 600;
    color: var(--ink-grey);
    line-height: 1.1;
  }
  .identity__role {
    font-size: 11px;
    color: var(--ink-light);
    margin-top: 4px;
  }
  .label {
    font-weight: 700;
    color: var(--ink-dark);
  }
  .contact {
    position: absolute;
    left: 300px;
    top: 328px;
    font-size: 11px;
    line-height: 13px;
    color: var(--ink-light);
    list-style: none;
  }
</style>
</head>
<body>
  <main class="canvas">
    <section class="card card--front" aria-label="Business card front">
      <div class="front-brand">t4 linkways</div>
      <div class="front-url">www.t4linkways.co.uk</div>
    </section>

    <section class="card card--back" aria-label="Business card back">
      <div class="back-brand">t4 linkways</div>
      <div class="back-rule"></div>
      <div class="identity">
        <div class="identity__name">Name</div>
        <div class="identity__role"><span class="label">Position / Job Title:</span> Network Consultant</div>
      </div>
      <ul class="contact">
        <li><span class="label">Mobile Phone Number:</span> +44 (0) 7700 900418</li>
        <li><span class="label">Land Line:</span> +44 (0) 1632 960274</li>
        <li><span class="label">Email Address:</span> name@t4linkways.co.uk</li>
        <li><span class="label">Web Site URL:</span> www.t4linkways.co.uk</li>
      </ul>
    </section>
  </main>
</body>
</html>
```